Raising Third Lantern Stewards (Book cover)

This project is for a book I am currently writing. It will help pastors and church leaders communicate why serving in the local church is the so important and how to motivate them to serve at high levels.

The title of the book comes from the passage of scripture where Jesus said, "when a solider demands you to carry his gear one mile, go with him two." He wants his followers to willingly do more than is expected. Doing the minimum seldom does much to change hearts of people around us.

This book will deal with these concepts and help leaders train others to follow in this line of thinking - to be Third Lantern Stewards.

Target Market(s)

church leaders, christian book readers

Industry/Entity Type

Church

Font styles to use
Sans Serif

Colors
fece3e

Requirements
Must have
• Catchy color, font layout to attract readers to take a 2nd look inside the book. Lots of empty space on the cover art, gradient color, sharp contrasts. Large Letters
Nice to have
• A central image on the artwork that will communicate the metaphor of going the 2nd mile.
Should not have
• any imagery that is suggestive

```html
<!DOCTYPE html>
<html lang="en">
<head>
<meta charset="utf-8">
<title>Raising Third Lantern Stewards — Book Cover</title>
<link rel="stylesheet" href="https://fonts.googleapis.com/css2?family=Red+Hat+Display:wght@700;900&family=Arimo:ital,wght@0,700;1,400&display=swap">
<style>
  :root {
    --stage: #eeeeee;
    --yellow-light: #fee066;
    --yellow: #fece3e;
    --yellow-deep: #f2b600;
    --red: #d93a2b;
    --ink: #1c1c1c;
    --white: #ffffff;
    --slab: #8a8a8a;
    --slab-light: #a3a3a3;
    --paper-text: #3a2f10;
  }
  * { box-sizing: border-box; margin: 0; padding: 0; }
  html, body { width: 1200px; height: 800px; overflow: hidden; }
  body {
    background: var(--stage);
    display: flex;
    align-items: center;
    justify-content: center;
    gap: 40px;
    font-family: "Red Hat Display", sans-serif;
  }
  .cover {
    position: relative;
    width: 400px;
    height: 600px;
    overflow: hidden;
    background: linear-gradient(180deg, var(--yellow-light) 0%, var(--yellow) 40%, var(--yellow-deep) 100%);
    box-shadow: 0 12px 30px rgba(0,0,0,0.12);
  }

  /* Back cover */
  .back-cover { text-align: center; padding: 52px 46px 0; color: var(--paper-text); }
  .back-cover__title {
    color: var(--red);
    font-weight: 900;
    font-size: 40px;
    letter-spacing: -0.5px;
    margin-bottom: 44px;
  }
  .back-cover__body {
    font-family: "Arimo", sans-serif;
    font-style: italic;
    font-size: 11.5px;
    line-height: 1.45;
    margin-bottom: 14px;
  }
  .back-cover__heading {
    font-weight: 700;
    font-size: 18px;
    color: var(--ink);
    margin: 24px 0 16px;
  }
  .back-cover__subheading {
    font-weight: 700;
    font-size: 12px;
    color: var(--ink);
    margin: 26px 0 8px;
  }
  .back-cover__note {
    font-family: "Arimo", sans-serif;
    font-style: italic;
    font-size: 10px;
  }

  /* Front cover */
  .front-cover__title {
    position: absolute;
    left: 54px;
    top: 62px;
    font-weight: 900;
    font-size: 38px;
    line-height: 0.98;
    letter-spacing: -0.8px;
    text-transform: uppercase;
  }
  .front-cover__title span { display: block; }
  .title-line--red { color: var(--red); }
  .title-line--white { color: var(--white); }
  .title-line--ink { color: var(--ink); }

  .front-cover__artwork {
    position: absolute;
    left: 0;
    top: 326px;
    width: 400px;
    height: 144px;
    background: linear-gradient(180deg, var(--slab-light) 0%, var(--slab) 100%);
  }

  .front-cover__author {
    position: absolute;
    left: 0; right: 0;
    top: 520px;
    text-align: center;
    font-weight: 900;
    font-size: 17px;
    letter-spacing: 0.5px;
  }
  .author-first { color: var(--red); }
  .author-last { color: var(--ink); }
</style>
</head>
<body>

  <section class="cover back-cover" aria-label="Back cover">
    <h2 class="back-cover__title">Back Cover</h2>
    <p class="back-cover__body">Every congregation rests on people who quietly give more than is asked. This book shows pastors and ministry leaders how to name that spirit, teach it with clarity, and build teams that serve gladly, faithfully and well beyond the minimum expected of them each week.</p>
    <p class="back-cover__body">Drawing on scripture and years of church life, it offers simple tools for calling, training and keeping volunteers who carry the load with joy.</p>
    <h3 class="back-cover__heading">Lorem Ipsum Dolor</h3>
    <p class="back-cover__body">A practical guide for anyone who longs to see serving become the heartbeat of the local church.</p>
    <h4 class="back-cover__subheading">Lorem ipsum</h4>
    <p class="back-cover__note">Short notes on the author go here.</p>
  </section>

  <section class="cover front-cover" aria-label="Front cover">
    <h1 class="front-cover__title">
      <span class="title-line--red">Raising</span>
      <span class="title-line--white">Third Lantern</span>
      <span class="title-line--ink">Stewards</span>
    </h1>

    <div class="front-cover__artwork" role="img" aria-label="Illustration: a robed figure walking along a long stepped stone ledge, going the second mile"></div>

    <p class="front-cover__author"><span class="author-first">AUTHOR'S</span> <span class="author-last">NAME</span></p>
  </section>

</body>
</html>
```